RWM Bricklaying business card

i need a business card designed for my bricklaying company.
I was also hoping to get a logo drawn up so i can put it on some t-shirts.
You can use any style or colours just as long as it lloks good. thanks Dallas

Dallas Whitby
RWM Bricklaying
0471395067
Any type of brick/blockwork
No job too small

```html
<!DOCTYPE html>
<html lang="en">
<head>
<meta charset="utf-8">
<title>RWM Bricklaying – Business Cards</title>
<link rel="stylesheet" href="https://fonts.googleapis.com/css2?family=Montserrat:wght@400;600;700&display=swap">
<style>
  :root {
    --backdrop: #ecedec;
    --card-white: #ffffff;
    --charcoal: #2b2a29;
    --brick-orange: #f07a1f;
    --text-light: #ffffff;
    --text-dark: #2b2a29;
  }
  * { box-sizing: border-box; margin: 0; padding: 0; }
  html, body {
    width: 1200px;
    height: 743px;
    overflow: hidden;
    background: var(--backdrop);
    font-family: "Montserrat", Arial, sans-serif;
  }
  .canvas { position: relative; width: 1200px; height: 743px; }

  .card {
    position: absolute;
    overflow: hidden;
    border-radius: 28px;
    background: var(--card-white);
    box-shadow: 0 6px 16px rgba(0,0,0,0.12);
  }
  .card > * { position: absolute; }

  /* Landscape card */
  .card--landscape { left: 69px; top: 170px; width: 621px; height: 390px; }
  .card--landscape .dark-panel { left: 0; top: 172px; width: 100%; height: 218px; background: var(--charcoal); }
  .card--landscape .accent-band { left: 0; top: 165px; width: 100%; height: 8px; background: var(--brick-orange); }
  .card--landscape .wordmark {
    left: 0; top: 40px; width: 100%; height: 90px;
    display: flex; align-items: center; justify-content: center; gap: 18px;
  }
  .wordmark__square { width: 46px; height: 46px; background: var(--brick-orange); }
  .wordmark__name { font-weight: 700; color: var(--text-dark); font-size: 44px; letter-spacing: 0.5px; }

  .contact { left: 0; width: 100%; text-align: center; }
  .contact__name { font-weight: 600; color: var(--brick-orange); font-size: 25px; }
  .contact__phone { display: flex; align-items: center; justify-content: center; gap: 10px; }
  .contact__tagline { font-weight: 600; color: var(--brick-orange); font-size: 18px; }

  .card--landscape .contact__name { top: 205px; }
  .card--landscape .contact__phone { top: 254px; font-weight: 700; color: var(--text-light); font-size: 25px; }
  .card--landscape .tagline-one { top: 327px; }
  .card--landscape .tagline-two { top: 364px; }
  .card--landscape .contact__name,
  .card--landscape .contact__phone,
  .card--landscape .contact__tagline { transform: translateY(-50%); }

  /* Portrait card */
  .card--portrait { left: 761px; top: 44px; width: 388px; height: 621px; }
  .card--portrait .dark-panel { left: 0; top: 0; width: 100%; height: 357px; background: var(--charcoal); }
  .card--portrait .accent-band { left: 0; top: 357px; width: 100%; height: 8px; background: var(--brick-orange); }
  .card--portrait .hero-art {
    left: 22px; top: 60px; width: 366px; height: 170px;
    background: linear-gradient(120deg, #3a3938 0%, #5a5957 60%, #4a4948 100%);
    border-radius: 6px 0 0 6px;
  }
  .card--portrait .wordmark {
    left: 0; top: 250px; width: 100%; height: 70px;
    display: flex; align-items: center; justify-content: center; gap: 12px;
  }
  .card--portrait .wordmark__square { width: 30px; height: 30px; }
  .card--portrait .wordmark__name { color: var(--text-light); font-size: 30px; }

  .card--portrait .contact__name { top: 413px; }
  .card--portrait .contact__phone { top: 459px; font-weight: 400; color: var(--text-dark); font-size: 23px; }
  .card--portrait .tagline-one { top: 523px; }
  .card--portrait .tagline-two { top: 559px; }
  .card--portrait .contact__name,
  .card--portrait .contact__phone,
  .card--portrait .contact__tagline { transform: translateY(-50%); }

  .phone-icon { width: 22px; height: 22px; }
</style>
</head>
<body>
<div class="canvas">

  <section class="card card--landscape" aria-label="RWM Bricklaying business card, landscape">
    <div class="wordmark">
      <span class="wordmark__square"></span>
      <span class="wordmark__name">RWM Bricklaying</span>
    </div>
    <div class="dark-panel"></div>
    <div class="accent-band"></div>
    <p class="contact contact__name">Dallas Whitby</p>
    <p class="contact contact__phone">
      <svg class="phone-icon" viewBox="0 0 24 24" aria-hidden="true">
        <path fill="#ffffff" d="M6.6 10.8a15.1 15.1 0 0 0 6.6 6.6l2.2-2.2a1 1 0 0 1 1-.25 11.4 11.4 0 0 0 3.6.57 1 1 0 0 1 1 1V20a1 1 0 0 1-1 1A17 17 0 0 1 3 4a1 1 0 0 1 1-1h3.5a1 1 0 0 1 1 1c0 1.25.2 2.45.57 3.57a1 1 0 0 1-.25 1z"/>
      </svg>
      0471395067
    </p>
    <p class="contact contact__tagline tagline-one">Any type of brick/blockwork</p>
    <p class="contact contact__tagline tagline-two">No job too small</p>
  </section>

  <section class="card card--portrait" aria-label="RWM Bricklaying business card, portrait">
    <div class="dark-panel"></div>
    <div class="hero-art" role="img" aria-label="Illustration of a bricklayer with a trowel beside an outlined brick wall"></div>
    <div class="wordmark">
      <span class="wordmark__square"></span>
      <span class="wordmark__name">RWM Bricklaying</span>
    </div>
    <div class="accent-band"></div>
    <p class="contact contact__name">Dallas Whitby</p>
    <p class="contact contact__phone">
      <svg class="phone-icon" viewBox="0 0 24 24" aria-hidden="true">
        <path fill="#f07a1f" d="M6.6 10.8a15.1 15.1 0 0 0 6.6 6.6l2.2-2.2a1 1 0 0 1 1-.25 11.4 11.4 0 0 0 3.6.57 1 1 0 0 1 1 1V20a1 1 0 0 1-1 1A17 17 0 0 1 3 4a1 1 0 0 1 1-1h3.5a1 1 0 0 1 1 1c0 1.25.2 2.45.57 3.57a1 1 0 0 1-.25 1z"/>
      </svg>
      0471395067
    </p>
    <p class="contact contact__tagline tagline-one">Any type of brick/blockwork</p>
    <p class="contact contact__tagline tagline-two">No job too small</p>
  </section>

</div>
</body>
</html>
```